Book Cover Design - Business/Self-Help Book

Book cover design for a business/self-help book. The title of the book is "OTTER Compass - Seven Quiet Habits of Steady Growth" It should also have "Unlock the Nine Hidden Keys Behind Lasting Momentum" as a subtitle somewhere.

Please see the website for an idea of the logo and sub-words: http://www.ottercompassbook.com

Book size will be 8.5" x 5.25"
Author info: Marlo Quindt

If your design includes a shark on the cover, it MUST be a hammerhead shark. Logo is attached.

I would like to stick with a red or orange theme like on the website but am open to any color idea. I like brighter colors and want the book to stand out and be attractive. If it's white, the wording and logo should be a bright color.

The back cover will just be preview text and selling points. It could have a picture in the background but will not have any pictures of the author.

If you include a spine design, please put the hammerhead logo on the spine.

Target Market(s)

Young Entrepreneurs and Business Professionals

Industry/Entity Type

Business

Requirements
Must have
• The hammerhead shark logo
Nice to have
• Look at the website - http://www.ottercompassbook.com
• It would be nice to have the six words throughout the cover similar to how it shows on the website cover picture.
Should not have
• Even though it caters to a younger crowd, it should not be cartoonish or child-like. Want a more serious and modern feel. Not too cluttered, i want the title to stand out and the shark to stand out.

```html
<!DOCTYPE html>
<html lang="en">
<head>
<meta charset="utf-8">
<title>OTTER Compass – Book Cover</title>
<link rel="stylesheet" href="https://fonts.googleapis.com/css2?family=Arimo:wght@400;700&family=Quicksand:wght@500;700&display=swap">
<style>
  :root {
    --page: #ffffff;
    --night: #0f1128;
    --night-deep: #161633;
    --sun: #f6d27a;
    --amber: #f0a25a;
    --ember: #e0603a;
    --crimson: #9e2436;
    --blot: #d9421c;
    --blot-dark: #b22a12;
    --tagline: #7a2a10;
    --band: #e8622a;
    --white: #ffffff;
  }
  * { box-sizing: border-box; margin: 0; padding: 0; }
  html, body {
    width: 1200px; height: 899px; overflow: hidden;
    background: var(--page);
    font-family: "Arimo", Arial, sans-serif;
  }
  .canvas { position: relative; width: 1200px; height: 899px; }

  .cover {
    position: absolute; left: 171px; top: 140px;
    width: 860px; height: 611px; overflow: hidden;
  }
  .cover-photo {
    position: absolute; inset: 0;
    background:
      radial-gradient(ellipse 260px 200px at 560px 340px, rgba(255,236,170,.9), rgba(255,236,170,0) 70%),
      linear-gradient(90deg, var(--night) 0%, var(--night-deep) 33%, #6a4050 40%, var(--sun) 50%, var(--amber) 68%, var(--ember) 88%, var(--crimson) 100%);
  }
  .cover-photo::after {
    content: ""; position: absolute; inset: 0;
    background: linear-gradient(180deg, rgba(0,0,0,0) 55%, rgba(90,20,40,.55) 100%);
  }

  .back-copy {
    position: absolute; left: 51px; top: 44px; width: 170px;
    color: var(--white); font-size: 7.6px; font-weight: 700;
    line-height: 15px; text-align: justify;
  }
  .back-copy p + p { margin-top: 15px; }
  .back-url {
    position: absolute; left: 143px; top: 547px;
    color: var(--white); font-size: 9px; font-weight: 700;
  }

  .spine-mark {
    position: absolute; left: 386px; top: 250px; width: 60px; height: 110px;
  }
  .spine-mark span {
    position: absolute; left: 50%; top: 50%;
    transform: translate(-50%, -50%) rotate(-90deg);
    white-space: nowrap; color: var(--white);
    font-family: "Quicksand", sans-serif; font-weight: 700; font-size: 11px;
  }

  .author-tab {
    position: absolute; left: 594px; top: -2px; width: 154px; height: 40px;
    background: var(--night-deep);
    border-radius: 0 0 77px 77px / 0 0 30px 30px;
    color: var(--white); font-size: 14px;
    display: flex; align-items: center; justify-content: center; padding-top: 2px;
  }
  .tagline {
    position: absolute; right: 57px; top: 54px;
    color: var(--tagline); font-family: "Quicksand", sans-serif;
    font-weight: 500; font-size: 17px;
  }
  .title-blot { position: absolute; left: 526px; top: 90px; width: 290px; height: 180px; }
  .title-name {
    position: absolute; left: 526px; top: 165px; width: 290px; text-align: center;
    color: var(--white); font-family: "Quicksand", sans-serif;
    font-weight: 700; font-size: 27px; letter-spacing: 0.3px; white-space: nowrap;
  }
  .subtitle {
    position: absolute; right: 22px; top: 485px; text-align: right;
    color: var(--white); font-size: 13px; line-height: 16px;
  }
  .elements-band {
    position: absolute; left: 483px; top: 535px; width: 377px; height: 36px;
    background: var(--band);
    clip-path: polygon(0 4%, 100% 0, 100% 70%, 96% 100%, 0 100%);
    color: var(--white); font-size: 10.5px;
    display: flex; align-items: center; padding-left: 14px; letter-spacing: 0.1px;
    white-space: nowrap;
  }
</style>
</head>
<body>
<div class="canvas">
  <section class="cover">
    <div class="cover-photo" role="img" aria-label="Sunset photograph with silhouette of a person holding up a glowing emblem between thumb and finger"></div>

    <div class="back-copy">
      <p>OTTER Compass is a name that gathers the seven quiet habits one needs to grow steadily in anything.</p>
      <p>It can be read as a formula, a map or a guide. There isn't a single key to growth but rather, progress is made up of these quiet areas.</p>
      <p>Ultimately, OTTER Compass is a philosophy and a way of life for high achievers, star athletes and thriving entrepreneurs. For those committed to personal development &amp; big goals, OTTER Compass is a blueprint and the primary starting point to mapping out the path to growth.</p>
      <p>To steadily reach any goal, there are six primary elements that must be understood and applied. These six elements are: Focus, Patience, Craft, Trust, Insight &amp; Resolve.</p>
    </div>
    <div class="back-url">www.ottercompassbook.com</div>

    <div class="spine-mark">
      <svg width="60" height="110" viewBox="0 0 60 110" role="img" aria-label="Soft red watercolour shape behind spine title">
        <ellipse cx="30" cy="55" rx="26" ry="52" fill="var(--blot)" opacity=".85"/>
      </svg>
      <span>OTTER COMPASS</span>
    </div>

    <div class="author-tab">Marlo Quindt</div>
    <div class="tagline">Seven Quiet Habits of Steady Growth</div>

    <svg class="title-blot" viewBox="0 0 290 180" role="img" aria-label="Layered red watercolour wash behind the title">
      <ellipse cx="145" cy="92" rx="142" ry="86" fill="var(--blot)" opacity=".8"/>
      <ellipse cx="160" cy="88" rx="110" ry="70" fill="var(--blot-dark)" opacity=".55"/>
    </svg>
    <div class="title-name">OTTER COMPASS</div>

    <div class="subtitle">Unlock the Nine Hidden Keys<br>Behind Lasting Momentum</div>
    <div class="elements-band">FOCUS + PATIENCE + CRAFT + TRUST + INSIGHT + RESOLVE</div>
  </section>
</div>
</body>
</html>
```